Wordpress Design For Virtual Assistant

I need a website design for my virtual assistant company, BrivoDesk. I would like to have a landing page, an about page, a page to list my services, contact us and FAQ. a blog page would be great as well.

It needs to be a modern, professional but fun look. Simple and easy to read and navigate. Colors used need to match the logo colors exactly with the red color being used only as a highlight/accept color.

I have uploaded an overview of BrivoDesk as well as my logo, copy of business card and stationary to give you an idea of the design style I prefer.

Industry/Entity Type

It Company

Coding

Coded - Design and coding required

Font styles to use
Sans Serif

Requirements
Must have
• Color scheme with exact logo colors
Nice to have
• www.plomquest.example/ can be used as an style inspiration

```html
<!DOCTYPE html>
<html lang="en">
<head>
<meta charset="utf-8">
<title>BrivoDesk – Virtual Assistants</title>
<link href="https://fonts.googleapis.com/css2?family=Lato:wght@300;400;700&family=Questrial&display=swap" rel="stylesheet">
<style>
:root{
  --teal:#2a9fa6;
  --green:#6bbf2c;
  --red:#d8412f;
  --ink:#2b2b2b;
  --text:#555;
  --grey:#efefef;
  --dark:#232323;
  --darker:#1b1b1b;
  --white:#fff;
}
*{box-sizing:border-box;margin:0;padding:0}
html,body{width:1200px;height:3896px;overflow:hidden}
body{font-family:'Lato',sans-serif;color:var(--text);background:var(--white);position:relative}
.color-bar{height:6px;background:linear-gradient(90deg,var(--green) 0 33%,var(--red) 33% 50%,var(--teal) 50% 100%)}
section,header,footer{position:relative;width:1200px;overflow:hidden}

/* header */
.site-header{height:150px}
.brand{position:absolute;left:78px;top:40px;display:flex;align-items:center;gap:12px}
.brand-mark{width:26px;height:26px;background:var(--red);border-radius:50%}
.brand-name{font-family:'Questrial',sans-serif;font-size:46px;color:var(--ink);font-weight:400}
.top-contact{position:absolute;right:78px;top:30px;display:flex;gap:40px;font-size:20px;color:var(--ink)}
.top-contact span{display:flex;align-items:center;gap:10px}
.top-contact svg{width:26px;height:26px}
.main-nav{position:absolute;right:78px;top:92px;display:flex;gap:42px;font-size:17px;color:var(--ink)}
.main-nav a{color:inherit;text-decoration:none;padding-bottom:14px}
.main-nav a.active{border-bottom:3px solid var(--teal)}

/* hero */
.hero{height:582px}
.hero-photo{position:absolute;inset:0;background:linear-gradient(100deg,#d9d2c8 0%,#f2f2f0 40%,#e4e8ea 70%,#b9c7a8 100%)}
.tagline{position:absolute;right:40px;bottom:30px;font-family:'Questrial',sans-serif;font-size:40px;font-weight:700;background:rgba(255,255,255,.85);padding:6px 18px}
.tagline .g{color:var(--green)}.tagline .r{color:var(--red)}.tagline .t{color:var(--teal)}

/* about */
.about{height:476px;background:var(--grey)}
.about-photo{position:absolute;right:0;top:0;width:560px;height:476px;background:linear-gradient(90deg,var(--grey),#d6d6d6 40%,#c9c9c9)}
.about-copy{position:absolute;left:78px;top:40px;width:640px}
.section-title{font-family:'Questrial',sans-serif;font-size:30px;color:var(--ink);padding-bottom:14px;border-bottom:1px solid #ccc;display:inline-block;width:330px}
.section-title b{font-weight:700}
.about-copy .lead{font-size:17px;line-height:1.5;margin-top:22px}
.about-copy .body{font-size:13px;line-height:1.65;margin-top:14px}
.about-copy .tail{font-size:14px;margin-top:34px}
.about-copy .tail a{color:var(--red);text-decoration:none}

/* details */
.details{height:550px;background:linear-gradient(90deg,#fafafa,#eaeaea)}
.details-photo{position:absolute;right:60px;top:0;width:520px;height:550px;background:linear-gradient(180deg,#d7d7d7,#bfbfbf 60%,#9fa4a8)}
.details-copy{position:absolute;left:78px;top:72px;width:560px}
.big-title{font-family:'Questrial',sans-serif;font-size:37px;color:var(--ink);line-height:1.3}
.big-title .accent{color:var(--teal);display:block}
.details-copy p{font-size:17px;line-height:1.65;color:var(--ink);margin-top:34px}
.btn-small{display:inline-block;background:var(--teal);color:var(--white);font-size:14px;font-weight:700;padding:8px 14px;margin-top:30px}

/* assistants */
.assistants{height:600px}
.assistant-photo{position:absolute;left:78px;top:24px;width:362px;height:560px;background:linear-gradient(180deg,#eee,#cfc9c4 55%,#2f2f2f)}
.assistant-copy{position:absolute;left:462px;top:68px;width:660px}
.benefit-list{list-style:none;margin-top:20px}
.benefit-list li{display:flex;align-items:center;gap:16px;font-size:17px;color:var(--ink);padding:12px 0;border-bottom:1px solid #ddd}
.benefit-list svg{width:18px;height:18px;flex:none}
.benefit-list .noicon{padding-left:34px}

/* consultation */
.consult{height:166px;background:var(--red);color:var(--white)}
.consult h2{position:absolute;left:78px;top:28px;font-family:'Questrial',sans-serif;font-weight:400;font-size:37px}
.consult p{position:absolute;left:78px;top:86px;width:820px;font-size:15px;line-height:1.5}
.btn-start{position:absolute;right:80px;top:50px;width:192px;height:48px;background:var(--green);font-size:18px;font-weight:700;display:flex;align-items:center;justify-content:center}

/* service tabs */
.service-tabs{height:136px;background:var(--darker);display:flex;padding-left:80px}
.tab{width:160px;display:flex;flex-direction:column;align-items:center;justify-content:center;gap:14px;color:var(--white);font-size:14px;font-weight:700;margin-right:4px}
.tab svg{width:40px;height:40px}
.tab.active{background:var(--green);margin-top:-10px}

/* content support */
.content-support{height:390px;background:linear-gradient(180deg,#2c2c2c,#3a3a3a);color:#ddd}
.content-support h2{text-align:center;font-family:'Questrial',sans-serif;font-weight:400;font-size:32px;color:var(--white);margin-top:40px}
.content-support h2 span{color:var(--green)}
.rule{width:150px;height:2px;background:var(--teal);margin:12px auto 0}
.content-support .intro{text-align:center;font-size:13.5px;line-height:1.7;width:1020px;margin:28px auto 0}
.feature-grid{display:grid;grid-template-columns:repeat(3,270px);gap:6px 20px;width:880px;margin:22px auto 0;font-size:15px;list-style:none}
.feature-grid li::before{content:"• "}
.benefits{position:absolute;left:0;right:0;top:286px;border-top:1px solid #555;padding-top:30px;display:flex;padding-left:226px;font-size:15px}
.benefits .label{color:var(--green);width:230px;line-height:1.6}
.benefits .label span{color:#ddd}
.benefits ul{list-style:none;line-height:1.7;width:380px}
.benefits li::before{content:"• "}

/* testimonials */
.testimonials{height:444px;text-align:center}
.testimonials h2{font-family:'Questrial',sans-serif;font-weight:400;font-size:30px;color:var(--ink);margin-top:40px}
.quotes{display:flex;justify-content:space-between;width:900px;margin:44px auto 0}
.quote{width:270px}
.avatar{width:86px;height:86px;border-radius:50%;background:linear-gradient(#c9c2bb,#8d8580);margin:0 auto}
.quote p{font-size:13.5px;line-height:1.6;color:var(--ink);margin-top:30px;padding-bottom:18px;border-bottom:1px solid #ccc}
.quote cite{display:block;font-style:normal;font-size:14px;margin-top:14px}
.quote cite b{color:var(--teal);font-weight:400}

/* footer */
.site-footer{height:318px;background:var(--dark);color:#999;font-size:13px}
.foot-brand{position:absolute;left:78px;top:30px;display:flex;align-items:center;gap:8px}
.foot-brand .brand-mark{width:16px;height:16px}
.foot-brand .brand-name{font-size:28px;color:var(--white)}
.foot-about{position:absolute;left:78px;top:96px;width:250px;line-height:1.55}
.foot-col{position:absolute;top:50px}
.foot-col h3{font-size:15px;color:var(--white);font-weight:700;padding-bottom:10px;border-bottom:2px solid var(--teal);display:inline-block;min-width:100px}
.foot-col ul{list-style:none;margin-top:16px;line-height:1.6}
.foot-col p{margin-top:16px;line-height:1.55}
.foot-col p b{color:#ccc}
.email-field{margin-top:22px;width:200px;height:34px;background:#3a3a3a;display:flex;align-items:center;gap:8px;padding-left:12px}
.btn-sub{margin-top:14px;width:104px;height:34px;background:var(--red);color:var(--white);font-weight:700;display:flex;align-items:center;justify-content:center}
.copyright{position:relative;height:72px;background:var(--darker);color:#999;font-size:13px}
.copyright p{position:absolute;left:78px;top:28px}
.social{position:absolute;right:78px;top:18px;display:flex;gap:14px}
.social span{width:36px;height:36px;border-radius:50%;background:var(--teal)}
.social span:last-child{background:var(--red)}
</style>
</head>
<body>
<div class="color-bar"></div>
<header class="site-header">
  <div class="brand"><span class="brand-mark"></span><span class="brand-name">BrivoDesk</span></div>
  <div class="top-contact">
    <span><svg viewBox="0 0 24 24"><circle cx="12" cy="12" r="12" fill="#222"/><path d="M8 6l2 0 1 3-1.5 1a7 7 0 0 0 4 4l1-1.5 3 1v2a2 2 0 0 1-2 2A10 10 0 0 1 6 8a2 2 0 0 1 2-2z" fill="#fff"/></svg>(555) 310-4827</span>
    <span><svg viewBox="0 0 24 24"><circle cx="12" cy="12" r="12" fill="#222"/><rect x="6" y="8" width="12" height="8" fill="#fff"/><path d="M6 8l6 5 6-5" stroke="#222" fill="none"/></svg>support@brivodesk.example</span>
  </div>
  <nav class="main-nav">
    <a class="active">Home</a><a>Who We Are</a><a>Our Services</a><a>Plans &amp; Pricing</a><a>FAQ's</a><a>Testimonials</a><a>Contact us</a>
  </nav>
</header>

<section class="hero">
  <div class="hero-photo" role="img" aria-label="Photo of two smiling business professionals in a bright office"></div>
  <div class="tagline"><span class="g">Expanding</span> <span class="r">•Business</span> <span class="t">•Virtually</span></div>
</section>

<section class="about">
  <div class="about-photo" role="img" aria-label="Photo of hands typing on a laptop"></div>
  <div class="about-copy">
    <h2 class="section-title">About <b>BrivoDesk</b></h2>
    <p class="lead">BrivoDesk is a virtual assistant specializing in comprehensive online marketing for small business owners and entrepreneurs.</p>
    <p class="body">BrivoDesk provides small business owners &amp; entrepreneurs with critical administrative, and management support, virtually. We offer a comprehensive, affordable way to grow your brand presence and compete with competitors, both large and small, by reaching your market virtually. This happens when the door to the digital revolution is unlocked and paired with a savvy digital strategy. We know it can be time consuming and confusing to stay organized and up to date in today's fast paced digital revolution. With that in mind, it is more crucial than ever to stay current in all of the rapidly changing aspects in technological advancement. That's where BrivoDesk comes to save the day with the newest, most cutting edge ways to help!</p>
    <p class="tail">Bills? Paid. Inbox? Cleared. Travel? Booked. <a>Learn more</a></p>
  </div>
</section>

<section class="details">
  <div class="details-photo" role="img" aria-label="Photo of a businessman in a suit using a tablet"></div>
  <div class="details-copy">
    <h2 class="big-title">We Handle Details So It Will<span class="accent">Go off Without a Hitch</span></h2>
    <p>BrivoDesk provides small business owners &amp; entrepreneurs with critical administrative, and management support, virtually. We offer a comprehensive, affordable way to grow your brand presence and compete with competitors, both large and small, by reaching your market virtually.<br>This happens when the door to the digital revolution is unlocked and paired with a savvy digital strategy.</p>
    <span class="btn-small">Learn More+</span>
  </div>
</section>

<section class="assistants">
  <div class="assistant-photo" role="img" aria-label="Photo of a smiling professional woman in a vest"></div>
  <div class="assistant-copy">
    <h2 class="big-title">Some People Call Them Super Human,<span class="accent">We Call Them Virtual Assistants</span></h2>
    <ul class="benefit-list">
      <li><svg viewBox="0 0 18 18"><path d="M2 9l5 5 9-11" stroke="#d8412f" stroke-width="3" fill="none"/></svg>Time spent interviewing and training new assistants. No turnover</li>
      <li><svg viewBox="0 0 18 18"><path d="M2 9l5 5 9-11" stroke="#d8412f" stroke-width="3" fill="none"/></svg>In office equipment/devices, supplies &amp; app costs</li>
      <li><svg viewBox="0 0 18 18"><path d="M2 9l5 5 9-11" stroke="#d8412f" stroke-width="3" fill="none"/></svg>Resources-employee management, physical space and training</li>
      <li class="noicon">Headache and drama of time management - with BD there is no down wasted/down time</li>
      <li><svg viewBox="0 0 18 18"><path d="M2 9l5 5 9-11" stroke="#d8412f" stroke-width="3" fill="none"/></svg>Save money on marketing firms that charge thousand</li>
    </ul>
    <span class="btn-small">Learn More+</span>
  </div>
</section>

<section class="consult">
  <h2>Free 30 Minute Consultation</h2>
  <p>We are happy to set up a free consultation with any interested prospect for the purposes of determining needs, ability, and brainstorming.</p>
  <div class="btn-start">Get Started</div>
</section>

<section class="service-tabs">
  <div class="tab active"><svg viewBox="0 0 40 40" fill="none" stroke="#fff" stroke-width="2"><rect x="8" y="5" width="22" height="28"/><path d="M13 13h12M13 19h12M13 25h8"/></svg>Content Support</div>
  <div class="tab"><svg viewBox="0 0 40 40" fill="none" stroke="#fff" stroke-width="2"><circle cx="20" cy="9" r="4"/><circle cx="9" cy="30" r="4"/><circle cx="31" cy="30" r="4"/><path d="M20 13v7M9 26v-6h22v6"/></svg>Office Organization</div>
  <div class="tab"><svg viewBox="0 0 40 40" fill="none" stroke="#fff" stroke-width="2"><circle cx="20" cy="12" r="5"/><path d="M10 32a10 10 0 0 1 20 0"/><circle cx="8" cy="16" r="3"/><circle cx="32" cy="16" r="3"/></svg>Business Consulting</div>
  <div class="tab"><svg viewBox="0 0 40 40" fill="none" stroke="#fff" stroke-width="2"><rect x="6" y="9" width="28" height="25"/><path d="M6 16h28M13 5v7M27 5v7"/></svg>Event Planning</div>
  <div class="tab"><svg viewBox="0 0 40 40" fill="none" stroke="#fff" stroke-width="2"><circle cx="20" cy="20" r="14"/><path d="M10 24l20-9-8 14-3-5z"/></svg>Travel Arrangements</div>
  <div class="tab"><svg viewBox="0 0 40 40" fill="none" stroke="#fff" stroke-width="2"><rect x="6" y="10" width="28" height="20"/><path d="M6 10l14 11 14-11"/></svg>Mailings</div>
</section>

<section class="content-support">
  <h2>Content <span>Support</span></h2>
  <div class="rule"></div>
  <p class="intro">Perfect your content and allow your documents, spreadsheets, budgets, inventory, accounts, reports, data analysis, presentations, cover letters, memos, meeting prep, notes, resumes, contracts, labels, event programs, and newsletters to help you be more efficient and unify brand to clients. (spreadsheets, slide decks, &amp; text files)</p>
  <ul class="feature-grid">
    <li>Create &amp; Update</li><li>Formula Integration</li><li>Custom Header/Footers</li>
    <li>Professional Formatting</li><li>Data Entry &amp; Editing</li><li>Simplify &amp; Improve</li>
  </ul>
  <div class="benefits">
    <div class="label">Content Support<br><span>Benefits:</span></div>
    <ul><li>Uniform business/company documents</li><li>Document efficiency optimized</li></ul>
    <ul><li>Saves Time</li><li>Electronically Savvy</li></ul>
  </div>
</section>

<section class="testimonials">
  <h2>What our Clients are saying</h2>
  <div class="rule"></div>
  <div class="quotes">
    <div class="quote"><div class="avatar" role="img" aria-label="Client portrait"></div><p>"Lorem ipsum dolor sit amet, consectetur adipiscing elit, sed do eiusmod tempor incididunt ut labore et dolore magna aliqua. Ut enim veniam, quis nostrud ...."</p><cite><b>Lena Marlow</b>, Speaker and Coach</cite></div>
    <div class="quote"><div class="avatar" role="img" aria-label="Client portrait"></div><p>"Lorem ipsum dolor sit amet, consectetur adipiscing elit, sed do eiusmod tempor incididunt ut labore et dolore magna aliqua. Ut enim veniam, quis nostrud ...."</p><cite><b>Devin Okafor</b>, Entrepreneur &amp; Marketing</cite></div>
    <div class="quote"><div class="avatar" role="img" aria-label="Client portrait"></div><p>"Lorem ipsum dolor sit amet, consectetur adipiscing elit, sed do eiusmod tempor incididunt ut labore et dolore magna aliqua. Ut enim veniam, quis nostrud ...."</p><cite><b>Paul Renner</b>, Founder, Quiet Harbor Living</cite></div>
  </div>
</section>

<footer class="site-footer">
  <div class="foot-brand"><span class="brand-mark"></span><span class="brand-name">BrivoDesk</span></div>
  <p class="foot-about">BrivoDesk provides a virtual, customizable array of services depending on the client and their business needs. Services include: content creation/support, virtual organization, business consulting, event planning, travel arrangements, and blast mailings just to name a few.</p>
  <div class="foot-col" style="left:426px"><h3>About Us</h3><ul><li>Who We Are</li><li>Our Services</li><li>Plans &amp; Pricing</li><li>FAQ's</li><li>Testimonials</li><li>Contact us</li></ul></div>
  <div class="foot-col" style="left:570px"><h3>Policies</h3><ul><li>Terms of Service</li><li>Privacy Policy</li><li>Security</li></ul></div>
  <div class="foot-col" style="left:710px;width:210px"><h3>Sign Up Newsletter</h3><p>Sign Up now for more information about our company!</p><div class="email-field">✉ Enter your Email</div><div class="btn-sub">Submit</div></div>
  <div class="foot-col" style="left:952px"><h3>Contact Us</h3><p><b>BrivoDesk</b><br>Lorem ipsum dolo, 1245<br><br>Phone:<br>(555) 310-4827<br><br>Email:<br>support@brivodesk.example</p></div>
</footer>
<div class="copyright">
  <p>Copyright © 2016 BrivoDesk. All Rights Reserved.</p>
  <div class="social"><span></span><span></span><span></span><span></span></div>
</div>
<div class="color-bar"></div>
</body>
</html>
```